Design a Full Page PDF Brochure "white paper" (Adobe InDesign)

Hello, my business needs a template to create "white papers" for our website. These are the free PDF downloads that you see on websites for lead capture.

The winning entry will need the following seven characteristics:
(1) A consistent color palette (or scheme) and feel of our website and logo (which I've attached). Even thought it is called a "white paper", please use lots of color and make it vibrant.
(2) A cover sheet that fills up the whole page, it also needs to have contact information on it (you can use this for now):

Ferris Oakhurst
48 Lindel Rd
Springfield, USA
414-362-8071
ferris@quabbleton.example
[login to view URL]

It's important that our logo is used as part of the cover page design. Feel free to be creative with this.

(3) The text needs to have different sized subheadings (H1, H2, H3)
(4) I would suggest adding "call outs" to highlight quotes from the text
(5) I would suggest submitting entries with multiple page layouts that can be used
(6) You may use Latin text and stock photos that I will replace. Our website [login to view URL] uses a theme of hiking, mountains, and paths.
(7) The final page needs to also have the contact information on it

To help clarify what I'm looking for, here are some examples of white papers:
[login to view URL]
[login to view URL]
[login to view URL]

The entries need to be in Adobe InDesign. The winner needs to turn over the final InDesign Files along with any supporting files such as in Adobe Illustrator.

Also, please do not contact me outside of Taskory (doing so will disqualify your entries).

Thank you ahead of time for your work.

```html
<!DOCTYPE html>
<html lang="en">
<head>
<meta charset="utf-8">
<title>Verdant Ridge Advisors — White Paper Spreads</title>
<link href="https://fonts.googleapis.com/css2?family=Titillium+Web:wght@300;400;600;700&family=Open+Sans:wght@400;600&display=swap" rel="stylesheet">
<style>
  :root{
    --green:#8cc43f;
    --green-dark:#6fa52a;
    --ink:#2a2b2d;
    --charcoal:#353638;
    --paper:#f5f6f8;
    --mist:#e4e7ec;
    --card:#e9ecf0;
    --rule:#c9ced6;
    --text:#5b6068;
    --stage:#ededee;
    --white:#ffffff;
  }
  *{box-sizing:border-box;margin:0;padding:0}
  html,body{width:1200px;height:3044px;overflow:hidden}
  body{background:var(--stage);font-family:"Open Sans",Arial,sans-serif;color:var(--text)}
  .canvas{position:relative;width:1200px;height:3044px}
  .spread{position:absolute;left:80px;width:1040px;height:700px;display:flex;box-shadow:0 18px 40px rgba(0,0,0,.16)}
  .spread-1{top:40px}.spread-2{top:788px}.spread-3{top:1536px}.spread-4{top:2284px}
  .page{position:relative;width:520px;height:700px;background:var(--paper);overflow:hidden}
  .page-left{box-shadow:inset -14px 0 18px -14px rgba(0,0,0,.25)}
  .page-right{box-shadow:inset 14px 0 18px -14px rgba(0,0,0,.2)}
  .abs{position:absolute}
  .shapes{position:absolute;inset:0;width:100%;height:100%}
  .folio{position:absolute;top:14px;width:14px;height:14px;background:var(--green);color:var(--white);font:600 7px/14px "Titillium Web",sans-serif;text-align:center;z-index:2}
  .page-left .folio{left:18px}.page-right .folio{right:18px}
  .web{position:absolute;top:16px;right:24px;font:400 7px "Titillium Web",sans-serif;color:#8b9098;letter-spacing:.3px;z-index:2}
  .photo{position:absolute}
  .kicker{font:300 13px/1 "Titillium Web",sans-serif;text-transform:uppercase;letter-spacing:1px}
  .h1{font:700 26px/1 "Titillium Web",sans-serif;text-transform:uppercase;letter-spacing:.5px}
  .h2{font:600 20px/1.05 "Titillium Web",sans-serif;text-transform:uppercase}
  .h3{font:600 12px/1.2 "Titillium Web",sans-serif;text-transform:uppercase;letter-spacing:.4px}
  .on-dark{color:var(--white)}
  .green{color:var(--green)}
  .ink{color:var(--ink)}
  .body{font-size:7.5px;line-height:1.55}
  .body p+p{margin-top:6px}
  .body-light{color:rgba(255,255,255,.92)}
  .brand{position:absolute;display:flex;align-items:center;gap:6px;font:600 15px/1 "Titillium Web",sans-serif;color:var(--green);text-transform:uppercase;letter-spacing:.6px}
  .brand-mark{width:10px;height:10px;background:var(--green)}
  .contact{position:absolute;font:400 7.5px/1.5 "Open Sans",sans-serif;color:var(--text)}
  .contact strong{font-weight:600;color:var(--ink)}
  .list{list-style:none;font-size:7.5px;line-height:1.65}
  .list li{padding-left:10px;position:relative}
  .list li::before{content:"";position:absolute;left:0;top:4px;width:4px;height:4px;background:var(--green)}
  .frame{position:absolute;border:1px solid var(--green)}
  .feature{margin-bottom:14px}
  .feature .h3{color:var(--white);margin-bottom:3px}
  .card{position:absolute;top:130px;width:130px;height:260px;background:var(--card)}
  .card-photo{height:70px;background:var(--green);display:flex;align-items:center;justify-content:center;font:400 8px "Titillium Web",sans-serif;color:rgba(255,255,255,.85);letter-spacing:1px}
  .card-name{margin-top:10px;font:700 10px "Titillium Web",sans-serif;color:var(--ink);text-transform:uppercase;text-align:center}
  .card-role{font:400 8px "Titillium Web",sans-serif;color:var(--text);text-align:center;margin-bottom:6px}
  .card .body{padding:0 10px}
  .bar{position:absolute;left:28px;width:200px;height:18px;background:var(--mist);font:600 7px/18px "Titillium Web",sans-serif;color:#7b8089;text-transform:uppercase;padding-left:10px;letter-spacing:.4px}
  .icon-tile{position:absolute;width:20px;height:20px;background:var(--green)}
  .tile{position:absolute;width:66px}
  .tile-photo{height:60px;background:linear-gradient(180deg,#4f9fe0,#9fd0f2 65%,#7fa86a)}
  .tile-label{margin-top:-22px;padding:0 4px;font:700 7px/1.05 "Titillium Web",sans-serif;color:var(--green);text-transform:uppercase;position:relative}
</style>
</head>
<body>
<main class="canvas">

  <!-- Spread 1: About / Charitable giving -->
  <section class="spread spread-1">
    <article class="page page-left">
      <svg class="shapes" viewBox="0 0 520 700" aria-hidden="true">
        <polygon points="0,0 520,0 520,120 0,150" fill="#2a2b2d"/>
        <polygon points="0,150 520,120 520,132 0,162" fill="#d6dae0"/>
      </svg>
      <div class="folio">01</div>
      <div class="abs" style="left:150px;top:30px">
        <div class="kicker on-dark">We make the</div>
        <div class="h1 on-dark" style="margin-top:2px">Complex Simple</div>
        <p class="body body-light" style="width:330px;margin-top:6px">Most people share one goal: steady progress and a plan that lasts, so they can enjoy the path and reach the summit with confidence.</p>
      </div>
      <div class="photo" role="img" aria-label="Hiker in a red jacket standing on a rock above the clouds under a blue sky" style="left:80px;top:105px;width:380px;height:165px;background:linear-gradient(180deg,#2d73c4 0%,#6fb0e6 55%,#d7e9f6 80%,#8a8f94 100%)"></div>
      <div class="abs" style="left:40px;top:185px;width:170px;height:150px;background:var(--green);padding:26px 18px">
        <div class="h2 on-dark" style="font-weight:300">About</div>
        <p class="body body-light" style="margin-top:10px">Verdant Ridge Advisors guides families and firms with clear, honest advice, helping each client plan well and move ahead with purpose.</p>
      </div>
      <div class="brand" style="left:60px;top:360px"><span class="brand-mark"></span>Verdant Ridge</div>
      <div class="contact" style="left:60px;top:384px;width:150px">
        <strong>Ferris Oakhurst</strong><br>48 Lindel Rd<br>Springfield, USA<br>414-362-8071<br>ferris@quabbleton.example<br>www.verdantridge.example
      </div>
      <div class="abs" style="left:225px;top:295px;width:265px">
        <div class="kicker green" style="font-size:11px">We make the</div>
        <div class="h2 green" style="margin-top:2px">Complex Simple</div>
        <div class="body" style="margin-top:12px">
          <p>Overall, our team takes every account into view, joining planning, tax and estate work into a single path that is easy to follow and simple to review each year.</p>
          <p>Security, performance and flexibility guide each plan. We listen first, then build a clear strategy that adapts as your goals and your family grow over time.</p>
          <p>Clear reports and steady contact keep every client informed, so decisions feel calm and well grounded.</p>
        </div>
      </div>
    </article>
    <article class="page page-right">
      <svg class="shapes" viewBox="0 0 520 700" aria-hidden="true">
        <polygon points="0,0 520,0 520,40 0,70" fill="#d6dae0"/>
        <polygon points="0,28 280,10 280,215 0,240" fill="#2a2b2d"/>
        <polygon points="280,60 520,46 520,280 470,380 280,200" fill="#8cc43f"/>
      </svg>
      <div class="folio">02</div>
      <div class="web">www.verdantridge.example</div>
      <div class="abs" style="left:40px;top:70px;width:220px">
        <div class="h1 on-dark" style="font-weight:600">Charitable</div>
        <div class="kicker on-dark" style="margin-top:2px">Giving</div>
        <p class="body body-light" style="margin-top:12px">Many clients choose to give back to the causes they care about. We help shape gifts that match your values, support your family and bring lasting good to your community.</p>
      </div>
      <div class="abs" style="left:320px;top:80px;width:170px">
        <div class="feature"><div class="h3">Overall 3-D</div><p class="body body-light">Every account viewed together, with one plan and one clear report.</p></div>
        <div class="feature"><div class="h3">Secure 2.0</div><p class="body body-light">Careful safeguards protect each step of your plan and your data.</p></div>
        <div class="feature"><div class="h3">Speed</div><p class="body body-light">Quick replies and timely reviews keep your plan moving.</p></div>
      </div>
      <div class="abs" style="left:40px;top:255px;width:250px">
        <div class="h2 green">Our Team</div>
        <p class="body" style="margin-top:10px">Our advisors bring years of planning work, joining tax, estate and investment skills so each client receives clear guidance from one trusted team.</p>
      </div>
      <div class="photo" role="img" aria-label="Man with arms spread wide standing on a green mountain ridge under a cloudy sky" style="left:40px;top:340px;width:150px;height:140px;background:linear-gradient(180deg,#5a9ad8 0%,#cfe3f3 45%,#7aa35a 70%,#4d7a3a 100%)"></div>
      <div class="body abs" style="left:205px;top:400px;width:240px">
        <p>Overall, our team reviews each account with care, setting clear steps and measuring progress through every season of life.</p>
        <p>Security, performance and flexibility shape our work, so plans can adapt as markets change and new goals appear.</p>
        <p>We keep in close touch and explain each choice in plain words.</p>
      </div>
    </article>
  </section>

  <!-- Spread 2: Approach / Implementation -->
  <section class="spread spread-2">
    <article class="page page-left">
      <svg class="shapes" viewBox="0 0 520 700" aria-hidden="true">
        <polygon points="0,0 520,0 520,40 0,55" fill="#d6dae0"/>
        <polygon points="0,40 320,28 320,140 0,160" fill="#2a2b2d"/>
        <polygon points="0,160 520,130 520,215 0,250" fill="#8cc43f"/>
      </svg>
      <div class="folio">03</div>
      <div class="abs" style="left:40px;top:58px;width:270px">
        <div class="kicker on-dark">Our</div>
        <div class="h1 on-dark">Approach</div>
        <p class="body body-light" style="margin-top:8px">We know that your goals and plans are unique. We begin by listening, then shape a clear path that fits your life and the way you like to work.</p>
      </div>
      <div class="photo" role="img" aria-label="Hiker with a blue backpack looking over a mountain valley" style="left:320px;top:50px;width:150px;height:170px;background:linear-gradient(180deg,#8cb3d8 0%,#c7d9e8 35%,#5f7a66 65%,#3d4f43 100%)"></div>
      <div class="abs" style="left:40px;top:180px;width:270px">
        <div class="h3 on-dark" style="font-size:13px">Implementation <span style="font-weight:700">Services</span></div>
        <p class="body body-light" style="margin-top:5px">Each plan is put in place with care, from first steps to yearly reviews.</p>
      </div>
      <div class="photo" role="img" aria-label="Person with arms raised on a metal walkway above snowy mountains" style="left:40px;top:270px;width:150px;height:180px;background:linear-gradient(180deg,#3f73b8 0%,#9cc4e8 50%,#dfe8ef 70%,#5b6168 100%)"></div>
      <div class="frame" style="left:170px;top:300px;width:300px;height:210px;border-top:none;border-right:none"></div>
      <div class="abs" style="left:210px;top:280px;width:250px">
        <div class="kicker green" style="font-size:10px">Implementation</div>
        <div class="h2 green" style="font-size:16px">Services Include</div>
        <ul class="list" style="margin-top:10px">
          <li>Retirement income planning and review</li>
          <li>Tax aware investment management</li>
          <li>Estate and legacy planning</li>
          <li>Education savings strategy</li>
          <li>Insurance and risk review</li>
          <li>Charitable giving plans</li>
          <li>Business succession planning</li>
          <li>Cash flow and budget guidance</li>
          <li>Family meetings and reporting</li>
          <li>Annual progress reviews</li>
        </ul>
      </div>
    </article>
    <article class="page page-right">
      <svg class="shapes" viewBox="0 0 520 700" aria-hidden="true">
        <polygon points="300,20 520,10 520,700 300,700" fill="#2f5fa0"/>
      </svg>
      <div class="folio" style="right:auto;left:18px">04</div>
      <div class="photo" role="img" aria-label="Sunset over a green mountain valley with scattered rocks" style="left:320px;top:30px;width:200px;height:670px;background:linear-gradient(180deg,#4a6fa8 0%,#e8b24a 25%,#f2d36b 32%,#86a94a 45%,#5f8f34 75%,#7a9a4a 100%)"></div>
      <div class="web" style="top:40px;color:var(--white)">www.verdantridge.example</div>
      <div class="frame" style="left:40px;top:50px;width:260px;height:110px"></div>
      <div class="abs" style="left:60px;top:60px;width:220px">
        <div class="kicker green" style="font-size:10px">Implementation</div>
        <div class="h2 green" style="font-size:16px">Services Include</div>
        <p class="body" style="margin-top:8px">Our planning services cover each part of your finances, joined in one plan and carried out by a team that knows you well.</p>
      </div>
      <p class="body abs" style="left:60px;top:190px;width:230px">We set up each account, move assets with care and confirm every detail, so your plan works as intended from day one and stays on track.</p>
      <div class="abs" style="left:40px;top:260px;width:280px;height:140px;background:var(--green);padding:20px 24px">
        <div class="body body-light">
          <p>We believe a good plan is simple to follow. Each step is explained, each result is measured and each review brings fresh clarity.</p>
          <p>In every season we stay close, adjusting the path as your needs change and new chances appear along the way.</p>
        </div>
      </div>
      <div class="abs" style="left:40px;top:420px;width:260px;height:90px;background:var(--charcoal);padding:16px 20px">
        <p style="font:600 9px/1.45 'Titillium Web',sans-serif;color:var(--white)">Our planning work is split into clear stages. We have helped many families reach their goals and we bring that same care to every plan.</p>
      </div>
      <div class="brand" style="left:350px;top:640px;color:var(--white)"><span class="brand-mark" style="background:var(--white)"></span>Verdant Ridge</div>
    </article>
  </section>

  <!-- Spread 3: Team -->
  <section class="spread spread-3">
    <article class="page page-left">
      <div class="photo" role="img" aria-label="Dark misty mountain peaks under grey sky" style="left:0;top:0;width:520px;height:175px;background:linear-gradient(180deg,#3b3d40 0%,#25272a 100%)"></div>
      <div class="folio">05</div>
      <div class="abs" style="left:40px;top:40px;width:420px">
        <div class="kicker on-dark">Our</div>
        <div class="h1 on-dark">Team</div>
        <p class="body body-light" style="margin-top:6px">Our team brings long experience in planning, tax and investment work. Together we give each client clear advice and steady support.</p>
      </div>
      <div class="card" style="left:45px">
        <div class="card-photo">PHOTO</div>
        <div class="card-name">Owen Hartley</div>
        <div class="card-role">Wealth Advisor</div>
        <p class="body">Owen helps families plan for retirement with clear steps and calm guidance.</p>
      </div>
      <div class="card" style="left:195px">
        <div class="card-photo">PHOTO</div>
        <div class="card-name">Ravi Kessler</div>
        <div class="card-role">Wealth Advisor</div>
        <p class="body">Ravi builds tax aware portfolios that balance growth with careful risk.</p>
      </div>
      <div class="card" style="left:345px">
        <div class="card-photo">PHOTO</div>
        <div class="card-name">Lena Marsh</div>
        <div class="card-role">Client Service Manager</div>
        <p class="body">Lena keeps every client informed and makes each review simple.</p>
      </div>
      <div class="photo" role="img" aria-label="Hiker with a backpack looking at snowy mountain peaks" style="left:0;top:470px;width:520px;height:230px;background:linear-gradient(180deg,#9cb4cc 0%,#dfe6ee 35%,#6f7e8c 65%,#3e4650 100%)"></div>
      <div class="abs" style="left:60px;top:450px;width:320px;height:50px;background:var(--green);padding:9px 20px">
        <div class="kicker on-dark" style="font-size:10px">We make</div>
        <div class="h3 on-dark" style="font-size:15px">The Complex Simple</div>
      </div>
      <div class="brand" style="left:330px;top:640px;color:var(--white)"><span class="brand-mark" style="background:var(--white)"></span>Verdant Ridge</div>
    </article>
    <article class="page page-right">
      <div class="folio" style="right:auto;left:18px">06</div>
      <div class="web">www.verdantridge.example</div>
      <div class="photo" role="img" aria-label="Lone hiker on a hillside at golden sunset" style="left:50px;top:40px;width:180px;height:140px;background:linear-gradient(180deg,#c98a54 0%,#e2b26e 40%,#7a5a3e 75%,#3e2f24 100%)"></div>
      <div class="abs" style="left:70px;top:150px;width:110px;height:48px;background:var(--green);padding:8px 14px">
        <div class="kicker on-dark" style="font-size:9px">Our</div>
        <div class="h3 on-dark" style="font-size:15px">Team</div>
      </div>
      <div class="body abs" style="left:40px;top:220px;width:210px">
        <p>Each advisor takes every account into view, joining planning work into one clear path that is simple to review.</p>
        <p>We measure progress often and share plain reports, so clients always know where they stand and what comes next on the road ahead.</p>
      </div>
      <div class="bar" style="top:380px">Takes into account additional payment</div>
      <div class="bar" style="top:402px">Takes into account additional payment</div>
      <div class="bar" style="top:424px">Takes into account additional payment</div>
      <div class="bar" style="top:446px">Takes into account additional payment</div>
      <p class="body abs" style="left:40px;top:480px;width:210px">Our reviews cover every account and each new goal, helping clients adjust their plans with confidence as life changes.</p>
      <div class="icon-tile" style="left:290px;top:90px"></div>
      <p class="body abs" style="left:300px;top:120px;width:180px">We review each account and new payment with care, keeping your plan current and simple to follow through every season of growth.</p>
      <div class="icon-tile" style="left:300px;top:250px"></div>
      <p class="body abs" style="left:310px;top:280px;width:170px">Clear reports show progress in plain words, so each decision feels calm, informed and well grounded in your goals.</p>
      <div class="icon-tile" style="left:310px;top:400px"></div>
      <p class="body abs" style="left:320px;top:430px;width:160px">Steady contact and quick replies keep your plan moving forward with care and purpose.</p>
    </article>
  </section>

  <!-- Spread 4: Nature / closing page with contact -->
  <section class="spread spread-4">
    <article class="page page-left">
      <div class="photo" role="img" aria-label="Two hikers crossing a wide snowfield below misty mountains" style="left:0;top:0;width:520px;height:700px;background:linear-gradient(180deg,#f3f5f7 0%,#dfe4ea 35%,#eef1f4 60%,#f7f8fa 100%)"></div>
      <div class="folio">07</div>
      <div class="abs" style="left:90px;top:40px;width:130px;height:220px;background:var(--green);padding:20px 18px">
        <div class="kicker on-dark" style="font-size:12px">We make</div>
        <div class="h2 on-dark" style="font-weight:700">The Complex</div>
        <div class="kicker on-dark" style="font-size:16px">Simple</div>
        <p class="body body-light" style="margin-top:12px">We take every account into view and join each part of your plan into one clear path you can follow.</p>
      </div>
      <div class="abs" style="left:250px;top:50px">
        <div class="kicker green" style="font-size:9px">We make</div>
        <div class="h3 green" style="font-size:13px">The Complex Simple</div>
      </div>
      <div class="tile" style="left:250px;top:88px"><div class="tile-photo" role="img" aria-label="Hiker on a rock under blue sky"></div><div class="tile-label">We make<br>the complex simple</div><p class="body" style="margin-top:10px">Clear plans that are simple to follow and review.</p></div>
      <div class="tile" style="left:330px;top:88px"><div class="tile-photo" role="img" aria-label="Hiker on a rock under blue sky"></div><div class="tile-label">We make<br>the complex simple</div><p class="body" style="margin-top:10px">Steady advice that grows with your family.</p></div>
      <div class="tile" style="left:250px;top:250px"><div class="tile-photo" role="img" aria-label="Hiker on a rock under blue sky"></div><div class="tile-label">We make<br>the complex simple</div><p class="body" style="margin-top:10px">Careful reviews that keep each goal on track.</p></div>
      <div class="tile" style="left:330px;top:250px"><div class="tile-photo" role="img" aria-label="Hiker on a rock under blue sky"></div><div class="tile-label">We make<br>the complex simple</div><p class="body" style="margin-top:10px">Plain reports that make decisions calm.</p></div>
      <div class="brand" style="left:70px;top:620px"><span class="brand-mark"></span>Verdant Ridge</div>
    </article>
    <article class="page page-right">
      <div class="photo" role="img" aria-label="Hiker in a red jacket standing on top of a rocky mountain summit under a cloudy sky" style="left:0;top:0;width:520px;height:700px;background:linear-gradient(180deg,#e6e9ed 0%,#c9cfd6 35%,#a9a79c 55%,#8d8a80 75%,#6f6e66 100%)"></div>
      <div class="folio" style="right:auto;left:18px">08</div>
      <div class="web">www.verdantridge.example</div>
      <div class="frame" style="left:40px;top:40px;width:440px;height:620px;border-color:rgba(140,196,63,.7)"></div>
      <div class="abs" style="left:330px;top:110px">
        <div class="kicker ink" style="font-size:11px">We make</div>
        <div class="h2 ink" style="font-weight:700">The Nature<br>Green!!!</div>
      </div>
      <div class="abs" style="left:280px;top:230px;width:200px;height:420px;background:var(--green);padding:22px 18px">
        <div class="body body-light">
          <p>We take every account into view and join planning, tax and estate work into one clear path that is easy to follow and review each year.</p>
          <p>Security, performance and flexibility guide our work. We listen first, then build a plan that adapts as your goals and family grow.</p>
          <p>Clear reports and steady contact keep every client informed, so each decision feels calm and well grounded.</p>
          <p>Together we reach the summit, step by steady step.</p>
        </div>
        <div class="abs" style="left:18px;bottom:22px;width:164px;border-top:1px solid rgba(255,255,255,.6);padding-top:10px">
          <div class="h3 on-dark" style="margin-bottom:4px">Contact</div>
          <p class="body body-light">Ferris Oakhurst<br>48 Lindel Rd<br>Springfield, USA<br>414-362-8071<br>ferris@quabbleton.example<br>www.verdantridge.example</p>
        </div>
      </div>
    </article>
  </section>

</main>
</body>
</html>
```